BrightLoop - IT services company
Refresh Stationary
Project: BrightLoop - IT services company
BrightLoop  - IT services company -
Creative Brief
Simple
Delia Okonjo
Marketing Manager
2418 Fenwick Lane Suite 140 Durham, NC 27705
delia.okonjo@brightloop-example.com
www.brightloop-example.com

```html
<!DOCTYPE html>
<html lang="en">
<head>
<meta charset="utf-8">
<title>BrightLoop Business Card</title>
<link href="https://fonts.googleapis.com/css2?family=Roboto+Condensed:wght@400;700&display=swap" rel="stylesheet">
<style>
  :root {
    --backdrop: #d9d9d9;
    --card-white: #ffffff;
    --brand-orange: #f26a2e;
    --brand-orange-light: #f7874f;
    --brand-navy: #1d3f6e;
    --text-grey: #6b6b6b;
    --shadow: rgba(0, 0, 0, 0.28);
  }
  * { margin: 0; padding: 0; box-sizing: border-box; }
  html, body {
    width: 1200px; height: 871px; overflow: hidden;
    background: var(--backdrop);
    font-family: "Roboto Condensed", Arial, sans-serif;
  }
  .stage {
    position: relative; width: 1200px; height: 871px;
    display: flex; align-items: center; justify-content: center; gap: 60px;
  }
  .card {
    position: relative; width: 500px; height: 286px;
    border-radius: 22px; overflow: hidden;
    box-shadow: 0 10px 24px var(--shadow);
  }
  .card--front { background: var(--card-white); }
  .card--back {
    background: linear-gradient(135deg, var(--brand-orange-light), var(--brand-orange));
    display: flex; flex-direction: column; align-items: center; justify-content: center;
  }
  .edge-stripe {
    position: absolute; left: 0; bottom: 0; width: 9px; height: 110px;
    background: var(--brand-orange);
  }
  .brand {
    display: flex; align-items: center; gap: 8px;
  }
  .brand__square { width: 22px; height: 22px; background: var(--brand-navy); }
  .brand__name {
    font-weight: 700; font-size: 26px; color: var(--brand-navy); line-height: 1;
  }
  .tagline {
    font-weight: 700; font-size: 10px; letter-spacing: 0.5px;
    color: var(--brand-orange); text-transform: uppercase; margin-top: 4px;
  }
  .card--front .brand-block { position: absolute; left: 34px; top: 84px; }
  .person { position: absolute; right: 38px; top: 96px; text-align: left; }
  .person__name { font-weight: 700; font-size: 19px; color: var(--brand-orange); }
  .person__title { font-size: 11px; color: var(--text-grey); margin-top: 2px; }
  .contact {
    position: absolute; left: 34px; bottom: 26px;
    font-size: 9.5px; line-height: 1.45; color: var(--text-grey); list-style: none;
  }
  .card--back .brand__square { width: 40px; height: 40px; background: var(--card-white); }
  .card--back .brand { gap: 14px; }
  .card--back .brand__name { font-size: 50px; color: var(--card-white); }
  .card--back .tagline { color: var(--card-white); font-size: 15px; margin-top: 8px; letter-spacing: 1px; }
</style>
</head>
<body>
<main class="stage">
  <section class="card card--front" aria-label="Business card front">
    <div class="brand-block">
      <div class="brand">
        <span class="brand__square"></span>
        <span class="brand__name">BrightLoop</span>
      </div>
      <p class="tagline">Managed IT Services</p>
    </div>
    <div class="person">
      <p class="person__name">Delia Okonjo</p>
      <p class="person__title">Marketing Manager</p>
    </div>
    <ul class="contact">
      <li>2418 Fenwick Lane Suite 140</li>
      <li>Durham, NC 27705</li>
      <li>Tel 919.555.0142</li>
      <li>Fax 919.555.0143</li>
      <li>Cell 919.555.0188</li>
      <li>delia.okonjo@brightloop-example.com</li>
      <li>www.brightloop-example.com</li>
    </ul>
    <span class="edge-stripe"></span>
  </section>
  <section class="card card--back" aria-label="Business card back">
    <div class="brand">
      <span class="brand__square"></span>
      <span class="brand__name">BrightLoop</span>
    </div>
    <p class="tagline">Managed IT Services</p>
  </section>
</main>
</body>
</html>
```